Ledgers On Track Business Card Design

We are a bookkeeping and accounting practice and are particularly passionate about Tallivo as 'state of the art' accounting software. We offer a number of services which are listed on the back of the card. The logos for LOT have already been developed. There are also other logos of organisations we are involved with - Tallivo (both certified advisor and silver partner), FKR, and dutyfile near. Regarding colours, we would like to use the colours similar to our website, www.ledgersontrack.com, and these connect with the www.tallivo.com.au website. The proposed layout as it is just does not look too great - it looks like an amateur has done it - which is true!

Industry/Entity Type

Accounting

Contact Information for Business Card

The details to appear on the card are found on the files uploaded. I have front and back rough layouts.

```html
<!DOCTYPE html>
<html lang="en">
<head>
<meta charset="utf-8">
<title>Ledgers On Track – Business Card</title>
<link rel="stylesheet" href="https://fonts.googleapis.com/css2?family=Arimo:wght@400;700&family=Questrial&display=swap">
<style>
  :root {
    --page: #f3f4f5;
    --card-white: #ffffff;
    --teal: #1b8c9c;
    --teal-dark: #0c7c8e;
    --rule: #1aa3c4;
    --ink: #3c3c3c;
    --ink-soft: #5a5a5a;
    --sky: #2fb4dc;
    --sky-light: #4cc6e8;
    --sea: #0f8aa6;
    --sea-deep: #0a6f86;
    --silver: #a9acaf;
    --white: #ffffff;
  }
  * { box-sizing: border-box; margin: 0; padding: 0; }
  html, body { width: 1200px; height: 900px; overflow: hidden; }
  body {
    background: var(--page);
    position: relative;
    font-family: "Questrial", "Century Gothic", sans-serif;
    color: var(--ink);
  }

  .card {
    position: absolute;
    top: 300px;
    width: 525px;
    height: 300px;
    border-radius: 24px;
    overflow: hidden;
    box-shadow: 0 14px 30px rgba(0,0,0,0.12);
  }

  /* Front */
  .card-front { left: 50px; background: var(--card-white); }
  .holder { position: absolute; right: 30px; top: 24px; text-align: right; }
  .holder-name { color: var(--teal); font-size: 17px; }
  .holder-line { font-size: 11.5px; color: var(--ink); margin-top: 3px; }

  .front-brand {
    position: absolute; left: 36px; top: 84px;
    display: flex; align-items: center; gap: 12px;
  }
  .brand-dot { width: 36px; height: 36px; border-radius: 50%; background: var(--teal); }
  .brand-name {
    font-family: "Arimo", Arial, sans-serif; font-weight: 700;
    font-size: 42px; color: var(--teal); letter-spacing: -0.5px;
  }
  .front-rule { position: absolute; left: 0; right: 0; top: 150px; height: 7px; background: var(--rule); }

  .contacts {
    position: absolute; left: 24px; top: 168px; list-style: none;
    font-size: 13px; line-height: 16.5px; color: var(--ink);
  }
  .contacts li { display: flex; align-items: center; gap: 5px; }
  .contacts svg { width: 12px; height: 12px; fill: var(--teal); flex: none; }
  .contacts .indent { padding-left: 17px; }
  .contacts .abn { padding-left: 17px; font-size: 9.5px; }

  .affiliations { position: absolute; right: 30px; top: 172px; width: 190px; }
  .software-row { display: flex; align-items: center; justify-content: flex-end; gap: 8px; }
  .partner-name { font-size: 18px; color: var(--sky); }
  .badge { width: 56px; height: 56px; border-radius: 50%; }
  .badge-advisor { background: var(--teal-dark); }
  .badge-plain { width: 22px; height: 22px; border-radius: 50%; background: var(--sky); }
  .member-name { text-align: right; margin-top: 8px; font-size: 17px; color: var(--sea-deep); }
  .institute { display: flex; align-items: center; justify-content: flex-end; gap: 8px; margin-top: 6px; }
  .institute-mark { width: 22px; height: 22px; border-radius: 50%; background: #e08a4a; }
  .institute-name { font-size: 22px; color: var(--ink-soft); }

  /* Back */
  .card-back { left: 625px; color: var(--white); }
  .back-backdrop {
    position: absolute; inset: 0;
    background: linear-gradient(115deg, var(--sky-light) 0%, var(--sky) 40%, var(--sea) 75%, var(--sea-deep) 100%);
  }
  .back-content { position: absolute; inset: 0; text-align: center; }
  .back-brand { margin-top: 32px; display: inline-flex; align-items: center; gap: 10px; }
  .back-brand .brand-dot { width: 26px; height: 26px; background: var(--white); }
  .back-brand .brand-name { font-size: 27px; color: var(--white); }
  .services {
    list-style: none; margin: 18px auto 0; width: 400px;
    font-family: "Questrial", sans-serif; font-size: 15px; line-height: 22.5px;
  }
  .back-partner {
    position: absolute; right: 24px; bottom: 92px;
    display: flex; align-items: center; gap: 8px;
  }
  .back-partner .partner-name { color: var(--white); font-size: 16px; }
  .badge-silver { width: 42px; height: 42px; border-radius: 50%; background: var(--silver); }
</style>
</head>
<body>

<article class="card card-front">
  <div class="holder">
    <p class="holder-name">Colin Marsh</p>
    <p class="holder-line">B Comm MA PhD AFKR</p>
    <p class="holder-line">Registered BAS agent</p>
  </div>

  <div class="front-brand">
    <span class="brand-dot"></span>
    <span class="brand-name">Ledgers On Track</span>
  </div>
  <div class="front-rule"></div>

  <ul class="contacts">
    <li><svg viewBox="0 0 12 12"><rect x="2.5" y="0.5" width="7" height="11" rx="1"/></svg>T 03 9555 0142</li>
    <li><svg viewBox="0 0 12 12"><path d="M2 1l2.5-.5 1.5 3-1.5 1c.6 1.4 1.6 2.4 3 3l1-1.5 3 1.5-.5 2.5C6 11 1 6 2 1z"/></svg>M 0400 555 318</li>
    <li><svg viewBox="0 0 12 12"><path d="M0 2.5h12v7H0z M0 2.5l6 4 6-4" stroke="#fff" stroke-width="0.8"/></svg>colin@ledgersontrack.com</li>
    <li><svg viewBox="0 0 12 12"><circle cx="6" cy="6" r="5.5"/><path d="M.5 6h11M6 .5v11" stroke="#fff" stroke-width="0.8"/></svg>www.ledgersontrack.com</li>
    <li><svg viewBox="0 0 12 12"><path d="M6 .5l5.5 5H10V11H7.5V8h-3v3H2V5.5H.5z"/></svg>18 Harlow Crescent,</li>
    <li class="indent">Brindle Park VIC 3090</li>
    <li class="abn">ABN 55 100 200 300</li>
  </ul>

  <div class="affiliations">
    <div class="software-row">
      <span class="partner-name">Tallivo</span>
      <span class="badge-plain"></span>
      <span class="badge badge-advisor"></span>
    </div>
    <p class="member-name">dutyfile near</p>
    <div class="institute">
      <span class="institute-mark"></span>
      <span class="institute-name">FKR</span>
    </div>
  </div>
</article>

<article class="card card-back">
  <div class="back-backdrop" role="img" aria-label="Decorative background of overlapping blue and teal curved bands"></div>
  <div class="back-content">
    <div class="back-brand">
      <span class="brand-dot"></span>
      <span class="brand-name">Ledgers On Track</span>
    </div>
    <ul class="services">
      <li>Bookkeeping – data entry, bank reconciliation and review</li>
      <li>Payroll – Tallivo Payroll Specialist</li>
      <li>BAS – FKR Public BAS Practitioner</li>
      <li>Training &amp; support – Tallivo Certified Advisor</li>
      <li>Management reports</li>
      <li>Tax – Dutyfile Near Member</li>
      <li>HR services</li>
    </ul>
  </div>
  <div class="back-partner">
    <span class="partner-name">Tallivo</span>
    <span class="badge-silver"></span>
  </div>
</article>

</body>
</html>
```